Report redesign

We need a designer to redesign the attached report and provide us with a template so we can use it for future reports. We want the redesigned report to look like the one in this link:

http://www3.quellbrix.org/docs/QBX_HVL_MPD_NewModelsAddressingSupplyChainTransportRisk_IndustryAgenda_2012.pdf

Colors
0392cd
3176b5
85acd3
85cae6
33a6d7
0292cd
33b8a4

```html
<!DOCTYPE html>
<html lang="en">
<head>
<meta charset="utf-8">
<title>Biomass Supply Assessment – Report Pages</title>
<link rel="stylesheet" href="https://fonts.googleapis.com/css2?family=Open+Sans:wght@400;600&display=swap">
<style>
:root{
  --ink:#4a5258;
  --title:#1aa6dd;
  --section:#3bd98a;
  --term:#2fb2e3;
  --rule:#7fd9ee;
  --page-border:#dfe3e6;
  --c1:#2f7fe3;
  --c2:#33aeea;
  --c3:#4cd0e6;
  --c4:#7fe2da;
}
*{box-sizing:border-box;margin:0;padding:0}
html,body{width:865px;height:1200px;overflow:hidden;background:#fff}
body{position:relative;font-family:"Open Sans",Arial,sans-serif;color:var(--ink)}
.page{position:absolute;width:405px;height:572px;background:#fff;border:1px solid var(--page-border)}
.p5{left:16px;top:17px}
.p6{left:440px;top:16px}
.p7{left:15px;top:607px;height:575px}
.p8{left:440px;top:598px;width:411px;height:583px}

.divider{position:absolute;top:35px;width:1px;background:var(--rule)}
.p5 .divider{left:262px;height:490px}
.p6 .divider{left:262px;height:500px}
.p8 .divider{left:355px;top:35px;height:515px}

.footer{position:absolute;bottom:26px;right:26px;font-size:4.2px;color:var(--rule);display:flex;gap:10px;align-items:center}
.footer .num{font-size:6px}
.footnote{position:absolute;bottom:28px;left:26px;font-size:4.4px;color:var(--ink)}

.page-title{position:absolute;font-size:10.5px;font-weight:600;color:var(--title);letter-spacing:.1px}
.p5 .page-title{left:25px;top:38px}
.p6 .page-title{left:25px;top:35px}

.toc{position:absolute;left:25px;top:63px;width:240px;font-size:6.1px;line-height:9px}
.p6 .toc{top:62px}
.toc-group{margin-bottom:9px}
.toc-row{display:flex}
.toc-row .pg{width:27px}
.toc-row.head{color:var(--section)}

.content{position:absolute;left:28px;top:33px;width:305px;font-size:6.2px;line-height:8.9px}
.h1{font-size:10.5px;font-weight:600;color:var(--title);margin-bottom:12px}
.h2{font-size:8.2px;font-weight:600;color:var(--section);margin:7px 0 7px}
.lead{margin-bottom:7px}
.goals{display:flex;gap:8px;margin:4px 0 12px 2px;align-items:flex-start}
.goal{border-radius:50%;display:flex;align-items:center;justify-content:center;text-align:center;color:#fff;font-size:5.6px;line-height:8px;padding:6px}
.goal.g1{width:56px;height:56px;background:var(--c1);margin-top:0}
.goal.g2{width:58px;height:58px;background:var(--c2);margin-top:20px}
.goal.g3{width:57px;height:57px;background:var(--c3)}
.goal.g4{width:58px;height:58px;background:var(--c4);margin-top:17px;font-size:5.2px}
.steps{list-style:none;margin-left:0}
.steps li{display:flex;padding:3px 0 3px 9px;border-bottom:1px solid var(--rule)}
.steps li .n{width:14px;flex:none}

.p8 .content{left:26px;top:32px;width:232px;font-size:5.9px;line-height:8.6px}
.p8 .h2{margin:0 0 17px}
.def{margin-bottom:9px}
.def .term{color:var(--term)}
</style>
</head>
<body>

<section class="page p5">
  <h2 class="page-title">TABLE OF CONTENTS</h2>
  <div class="divider"></div>
  <div class="toc">
    <div class="toc-group"><div class="toc-row head"><span class="pg">3</span><span>Executive Summary</span></div></div>
    <div class="toc-group">
      <div class="toc-row head"><span class="pg">6</span><span>1.0 Introduction</span></div>
      <div class="toc-row"><span class="pg">6</span><span>1.1 Objectives</span></div>
      <div class="toc-row"><span class="pg">6</span><span>1.2 Scope of Work</span></div>
      <div class="toc-row"><span class="pg">7</span><span>1.3 Definitions and Assumptions</span></div>
    </div>
    <div class="toc-group">
      <div class="toc-row head"><span class="pg">8</span><span>2.0 Wood Fibre Categories</span></div>
      <div class="toc-row"><span class="pg">8</span><span>2.1 Pulpwood</span></div>
      <div class="toc-row"><span class="pg">8</span><span>2.2 Clean Chip</span></div>
      <div class="toc-row"><span class="pg">8</span><span>2.3 Sawdust</span></div>
      <div class="toc-row"><span class="pg">8</span><span>2.4 Shavings</span></div>
    </div>
    <div class="toc-group">
      <div class="toc-row head"><span class="pg">9</span><span>3.0 Standing Timber Analysis</span></div>
      <div class="toc-row"><span class="pg">9</span><span>3.1 Public Lands</span></div>
      <div class="toc-row"><span class="pg">10</span><span>3.1.1 Hardwood Species Distribution</span></div>
      <div class="toc-row"><span class="pg">14</span><span>3.1.2 Age Class Distribution</span></div>
      <div class="toc-row"><span class="pg">18</span><span>3.1.3 Projected Usage</span></div>
      <div class="toc-row"><span class="pg">20</span><span>3.1.4 Net Potential Availability</span></div>
      <div class="toc-row"><span class="pg">22</span><span>3.1.5 Access to Crown Forest Resources</span></div>
      <div class="toc-row"><span class="pg">23</span><span>3.2 Private Lands</span></div>
    </div>
    <div class="toc-group">
      <div class="toc-row head"><span class="pg">24</span><span>4.0 Supply</span></div>
      <div class="toc-row"><span class="pg">24</span><span>4.1 Summary of Project Available Wood Fibre</span></div>
      <div class="toc-row"><span class="pg">25</span><span>4.1.1 Total Quantity of Project Available Clean Chip</span></div>
      <div class="toc-row"><span class="pg">26</span><span>4.1.2 Quantity and Cost for each Category of Clean Chip</span></div>
      <div class="toc-row"><span class="pg">27</span><span>4.1.3 Weighted Average Cost of Clean Chip by Category</span></div>
      <div class="toc-row"><span class="pg">28</span><span>4.1.4 Variation in the Cost of Clean Chip</span></div>
      <div class="toc-row"><span class="pg">28</span><span>4.1.5 Quantity and Cost of Sawmill Residual</span></div>
      <div class="toc-row"><span class="pg">29</span><span>4.2 Supply Curve</span></div>
      <div class="toc-row"><span class="pg">31</span><span>4.3 Potential Suppliers</span></div>
      <div class="toc-row"><span class="pg">39</span><span>4.3.1 Class A Suppliers</span></div>
      <div class="toc-row"><span class="pg">39</span><span>4.3.2 Class B Suppliers</span></div>
    </div>
    <div class="toc-group">
      <div class="toc-row head"><span class="pg">40</span><span>5.0 Competition4</span></div>
      <div class="toc-row"><span class="pg">40</span><span>5.1 Summary of Competitors</span></div>
      <div class="toc-row"><span class="pg">42</span><span>5.2 Competitor Profiles</span></div>
    </div>
    <div class="toc-group">
      <div class="toc-row head"><span class="pg">49</span><span>6.0 Conclusions</span></div>
      <div class="toc-row"><span class="pg">49</span><span>6.1 Summary of Quantity and Cost of Project Available Wood Fibre</span></div>
      <div class="toc-row"><span class="pg">50</span><span>6.2 Potential Availability of Additional Wood Fibre from suppliers</span></div>
      <div class="toc-row"><span class="pg">50</span><span>6.3 Summary of Competitors</span></div>
      <div class="toc-row"><span class="pg">50</span><span>6.4 Contract Chipping</span></div>
      <div class="toc-row"><span class="pg">51</span><span>6.5 Contract Establishment and Negotiations</span></div>
      <div class="toc-row"><span class="pg">51</span><span>6.6 Vertical Integration</span></div>
      <div class="toc-row"><span class="pg">51</span><span>6.7 Roundwood Intake Requires Licence from OMLF</span></div>
      <div class="toc-row"><span class="pg">52</span><span>6.8 Transportation Logistics</span></div>
      <div class="toc-row"><span class="pg">53</span><span>6.9 Seasonal Logging and Trucking Considerations</span></div>
      <div class="toc-row"><span class="pg">53</span><span>6.10 Harvesting Poplar Pulpwood for the Benefit of Forest Health</span></div>
      <div class="toc-row"><span class="pg">54</span><span>6.11 Short Haul Advantage</span></div>
      <div class="toc-row"><span class="pg">54</span><span>6.12 Study Limitations</span></div>
      <div class="toc-row"><span class="pg">54</span><span>6.13 Report as a Snapshot in Time</span></div>
    </div>
  </div>
  <div class="footer"><span>Biomass Supply Assessment – Collingwood, ON</span><span class="num">5</span></div>
</section>

<section class="page p6">
  <h2 class="page-title">TABLE OF CONTENTS</h2>
  <div class="divider"></div>
  <div class="toc">
    <div class="toc-group">
      <div class="toc-row head"><span class="pg">55</span><span>7.0 Next Steps</span></div>
      <div class="toc-row"><span class="pg">55</span><span>7.1 Fibre Procurement Plan</span></div>
      <div class="toc-row"><span class="pg">55</span><span>7.2 Draft Supply Contract</span></div>
      <div class="toc-row"><span class="pg">55</span><span>7.3 Biomass Supply Insurance</span></div>
      <div class="toc-row"><span class="pg">56</span><span>7.4 Biomass Procurement Management Services</span></div>
      <div class="toc-row"><span class="pg">56</span><span>7.5 Ontario Poplar Availability Study</span></div>
      <div class="toc-row"><span class="pg">57</span><span>Appendix A: Consulting Team</span></div>
      <div class="toc-row"><span class="pg">58</span><span>Appendix B: List of Contacted Suppliers</span></div>
    </div>
  </div>
  <div class="footer"><span>Biomass Supply Assessment – Collingwood, ON</span><span class="num">6</span></div>
</section>

<section class="page p7">
  <div class="content">
    <h1 class="h1">1.0 INTRODUCTION</h1>
    <p class="lead">Northvale Renewables Inc. (Northvale) engaged Timberline Analytics Inc. (Timberline) to conduct a study of wood fibre availability, cost and sourcing strategies to support the development of a proposed lignocellulosic ethanol plant in Collingwood, ON.</p>
    <h2 class="h2">1.1 OBJECTIVES</h2>
    <p>This study represents an assessment of Hardwood project availability (with a focus on Poplar), sustainability, logistics, and procurement strategies for sourcing between 22,000 and 44,000 bone dry metric tons per year (BDMT/yr) within a 4 hour drive-time distance of Collingwood, ON.</p>
    <div class="goals">
      <div class="goal g1">To evaluate the project's access</div>
      <div class="goal g2">To identify and vet potential suppliers</div>
      <div class="goal g3">To assess competion</div>
      <div class="goal g4">To recommend fibre sourcing strategies and logistical solutions.</div>
    </div>
    <p>The main objectives of this report are:</p>
    <ul class="steps">
      <li><span class="n">1.</span><span>To evaluate the project's access to a long-term, sustainable supply of Hardwood /feedstock;</span></li>
      <li><span class="n">2.</span><span>To identify and vet potential suppliers with whom Northvale can negotiate supply agreements;</span></li>
      <li><span class="n">3.</span><span>To assess competition in the woodshed and better understand current market and material flows;</span></li>
      <li><span class="n">4.</span><span>To recommend fibre sourcing strategies and logistical solutions.</span></li>
    </ul>
    <h2 class="h2" style="margin-top:12px">1.2 SCOPE OF WORK</h2>
    <p>To complete the study, Timberline conducted the following activities:</p>
    <ul class="steps">
      <li><span class="n">1.</span><span>Extracted a list of all known fibre suppliers within a 4 hour drive-time distance around Collingwood, ON from the Fibre Source Registry™, Timberline's proprietary database of wood suppliers and buyers in North America;</span></li>
      <li><span class="n">2.</span><span>Contacted all major suppliers within a 4 hour drive-time distance around Collingwood, ON (Map 8), to determine a) categories of wood fibre available; b) estimated availability by category; c) current delivered pricing by category; d) potential commitments to other buyers.</span></li>
      <li><span class="n">3.</span><span>Contacted all major competitors for wood fibre within a 6 hour drive-time distance around Collingwood, ON (Map 9), to determine a) categories of wood fibre consumed; b) quantities of wood fibre consumed; c) price paid for wood fibre.</span></li>
      <li><span class="n">4.</span><span>Aggregated and analyzed all data to derive total availability and average weighted cost figures, feedstock supply curves, and sensitivity / risk analyses.</span></li>
      <li><span class="n">5.</span><span>Aggregated and analyzed forest inventory data.</span></li>
    </ul>
  </div>
  <p class="footnote">Equivalent to 44,000 - 88,000 green metric tons per year (GMT/yr).</p>
  <div class="footer"><span>Biomass Supply Assessment – Collingwood, ON</span><span class="num">7</span></div>
</section>

<section class="page p8">
  <div class="divider"></div>
  <div class="content">
    <h2 class="h2">1.3 DEFINITIONS AND ASSUMPTIONS</h2>
    <p class="def"><span class="term">Bone Dry Metric Tons (BDMT)</span> - A measure of the weight of wood fibre that excludes the associated moisture content. For the purposes of this report, all quantity and cost figures have been expressed on a BDMT basis.</p>
    <p class="def"><span class="term">Class 1 Supplier</span> - Companies with 5,000 BDMT/yr or more of project available wood fibre.</p>
    <p class="def"><span class="term">Class 2 Supplier</span> - Companies with less than 5,000 BDMT/yr of project available wood fibre.</p>
    <p class="def"><span class="term">Competition Zone</span> - The competition zone for this project is defined by a 6 hour drive-time distance around Collingwood, ON.</p>
    <p class="def"><span class="term">Feedstock Capacity</span> - Northvale indicated that the required quantity of Hardwood feedstock for the project is estimated between 44,000 and 88,000 green tons per year (GMT/yr). When converted to bone dry tons, the estimated feedstock capacity is between 22,000 and 44,000 BDT/yr (assuming 50% moisture content of feedstock).</p>
    <p class="def"><span class="term">Forest Management Unit (FMU)</span> - An area defined by the OMLF used to divide the Crown (public) forests into smaller manageable units.</p>
    <p class="def"><span class="term">Green Metric Tons (GMT)</span> - A measure of material weight that includes both the wood fibre and moisture content components.</p>
    <p class="def"><span class="term">Metric Tons</span> - All wood fibre availability figures for this study are expressed in metric tons (MT) unless otherwise indicated. The following conversion factor was applied to data received in short tons (ST): 1 ST = 0.907185 MT.</p>
    <p class="def"><span class="term">Moisture Content</span> - For cases where potential suppliers could not offer data on the moisture content of available Hardwood fibre, the research team assumed a moisture content of 45%-50% for green fibre such as Clean Chip, and 15%-20% for dry fibre such as Shavings.</p>
    <p class="def"><span class="term">Ontario Ministry of Lands and Forestry (OMLF)</span> - The ministry responsible for managing timber resources in Ontario.</p>
    <p class="def" style="margin-bottom:0"><span class="term">Pulpwood Conversions</span> - It was assumed that 1 cubic metre of timber is equal to 1 green metric ton.</p>
    <p>Woodshed - The size of the woodshed, or supply zone, for this project is defined by a 4 hour drive-time distance around Collingwood, ON.</p>
  </div>
  <div class="footer"><span>Biomass Supply Assessment – Collingwood, ON</span><span class="num">8</span></div>
</section>

</body>
</html>
```